Business card design and logo for plumbing bussiness

We are wanting a logo for a plumbing business is Queensland Australia. KRV Plumbing and Drainage will be doing works on domestic and commercial sites.
Plumbing, drainage and gas works. We are wanting something that will stand out and be noticed. Colours could be black blue and white but open for suggestions.

Target Market(s)

Builders and home renovators

Industry/Entity Type

Plumbing

Contact Information for Business Card

Miles Dorgan - Director
0417 582 913
miles@krvplumbing.example.com.au
QBCC: 847 2106
ABN: 52 319 407 281

Font styles to use
Sans Serif

Colors
000000

Requirements
Must have
• Clear defined branding

```html
<!DOCTYPE html>
<html lang="en">
<head>
<meta charset="utf-8">
<title>KRV Plumbing and Drainage – Business Card</title>
<link rel="stylesheet" href="https://fonts.googleapis.com/css2?family=Open+Sans:wght@300;400;600;700&display=swap">
<style>
  :root {
    --backdrop: #3d3632;
    --card: #0b0b0b;
    --card-edge: #1c1c1c;
    --brand-blue: #1aa3e8;
    --ink-white: #f2f2f2;
    --ink-silver: #c9c9c9;
    --divider: #3a3a3a;
  }
  * { box-sizing: border-box; margin: 0; padding: 0; }
  html, body {
    width: 1200px;
    height: 900px;
    overflow: hidden;
    background: var(--backdrop);
    font-family: "Open Sans", Arial, sans-serif;
  }
  .stage {
    position: relative;
    width: 1200px;
    height: 900px;
  }
  .card {
    position: absolute;
    width: 520px;
    height: 318px;
    background: var(--card);
    border: 1px solid var(--card-edge);
    box-shadow: 0 10px 24px rgba(0, 0, 0, 0.45);
  }
  /* contact side */
  .card--back { left: 50px; top: 320px; }
  .card--back .brand-panel {
    position: absolute;
    left: 0; top: 0;
    width: 200px; height: 100%;
    display: flex;
    align-items: center;
    justify-content: center;
    gap: 10px;
  }
  .brand-panel .brand-dot {
    width: 18px; height: 18px;
    border-radius: 50%;
    background: var(--brand-blue);
  }
  .brand-panel .brand-name {
    color: var(--brand-blue);
    font-weight: 700;
    font-size: 19px;
    line-height: 1.2;
  }
  .card--back .divider {
    position: absolute;
    left: 200px; top: 60px;
    width: 1px; height: 198px;
    background: var(--divider);
  }
  .contact {
    position: absolute;
    left: 236px; top: 62px;
    color: var(--ink-white);
  }
  .contact .person-name {
    color: var(--brand-blue);
    font-weight: 700;
    font-size: 21px;
    line-height: 1.2;
  }
  .contact .person-role {
    font-size: 14px;
    margin-top: 2px;
  }
  .contact .registrations {
    margin-top: 20px;
    font-size: 14px;
    line-height: 1.55;
  }
  .registrations .label {
    color: var(--brand-blue);
    font-weight: 700;
  }
  .contact .lines {
    margin-top: 18px;
    font-size: 14px;
    line-height: 1.7;
    list-style: none;
  }
  .lines li {
    display: flex;
    align-items: center;
    gap: 8px;
    white-space: nowrap;
  }
  .lines svg { width: 12px; height: 12px; fill: var(--brand-blue); flex: none; }

  /* brand side */
  .card--front { left: 630px; top: 260px; }
  .card--front .wordmark {
    position: absolute;
    inset: 0;
    display: flex;
    align-items: center;
    justify-content: center;
    color: var(--ink-silver);
    font-weight: 300;
    font-size: 48px;
    letter-spacing: 0.5px;
  }
</style>
</head>
<body>
<main class="stage">
  <section class="card card--back">
    <div class="brand-panel">
      <span class="brand-dot"></span>
      <span class="brand-name">KRV Plumbing</span>
    </div>
    <div class="divider"></div>
    <div class="contact">
      <p class="person-name">Miles Dorgan</p>
      <p class="person-role">Director</p>
      <p class="registrations">
        <span class="label">QBCC:</span> 847 2106<br>
        <span class="label">ABN:</span> 52 319 407 281
      </p>
      <ul class="lines">
        <li>
          <svg viewBox="0 0 24 24" aria-hidden="true"><path d="M6.6 10.8a15.1 15.1 0 0 0 6.6 6.6l2.2-2.2a1 1 0 0 1 1-.25 11.4 11.4 0 0 0 3.6.57 1 1 0 0 1 1 1V20a1 1 0 0 1-1 1A17 17 0 0 1 3 4a1 1 0 0 1 1-1h3.5a1 1 0 0 1 1 1c0 1.25.2 2.45.57 3.57a1 1 0 0 1-.25 1z"/></svg>
          0417 582 913
        </li>
        <li>
          <svg viewBox="0 0 24 24" aria-hidden="true"><path d="M2 5h20v14H2z M2 5l10 8 10-8" /></svg>
          miles@krvplumbing.example.com.au
        </li>
      </ul>
    </div>
  </section>

  <section class="card card--front">
    <p class="wordmark">KRV Plumbing</p>
  </section>
</main>
</body>
</html>
```